Marlow Realty Real Estate Brokerage Recruiting Flyer

We are a real estate brokerage looking to hire more real estate agents. We need to list everything we have to offer as a company so real estate agents will join our company. this is our company website: www.Marlowrealty.example .

100% COMMISSION NO MONTHLY FEE
$450 Flat Transaction FEE

What We Offer:
24/7 Office Access
Free E & O Insurance for 1st Year
Free Online CE and PLE
Free 1,000 Business Cards
Free Professional Social Media Marketing
Free Printing, Scanning, and Copies
Free Buyer and Seller Presentation Packages
Free Filquay Cloud Based Document Management Access
Access to our Internal Brokerage Forum
Company Profit Sharing!
Private Offices Available to Rent

*Lead Generation Software with over 3,000 Leads
*10 Leads to Start
* Free Personal CRM and Website
*Restrictions and Rules apply

Company Address:
4817 Amberfield Road
Suite 512
Fairfax, VA 22194
Phone: 703-555-0147
email: info@marlowrealty.example

Target Market(s)

Real Estate Agents

Industry/Entity Type

Real Estate

Colors
0555a3
ffffff

Requirements
Must have
• 100% COMMISSION NO MONTHLY FEE
$450 Flat Transaction FEE

What We Offer:
24/7 Office Access
Free Online CE and PLE
Free 1,000 Business Cards
Company Profit Sharing!

*10 Leads to Start

Company Address:
4817 Amberfield Road
Suite 512
Fairfax, VA 22194
Phone: 703-555-0147

```html
<!DOCTYPE html>
<html lang="en">
<head>
<meta charset="utf-8">
<title>Marlow Realty – Agent Recruiting Flyer</title>
<link rel="stylesheet" href="https://fonts.googleapis.com/css2?family=Jost:wght@400;500;700&family=Roboto+Condensed:wght@400;700&display=swap">
<style>
  :root {
    --navy: #1f3a6e;
    --navy-deep: #172c57;
    --hero: #1b2f5c;
    --white: #ffffff;
    --ink: #1c2233;
    --grey: #d9dadd;
    --grey-line: #b9bcc4;
  }
  * { margin: 0; padding: 0; box-sizing: border-box; }
  html, body { width: 927px; height: 1200px; overflow: hidden; background: var(--white); }
  .flyer { position: relative; width: 927px; height: 1200px; overflow: hidden; font-family: "Roboto Condensed", Arial, sans-serif; color: var(--ink); }

  /* Header */
  .brand { position: absolute; top: 0; left: 0; width: 927px; height: 145px; display: flex; align-items: center; justify-content: center; gap: 12px; }
  .brand-mark { width: 26px; height: 26px; background: var(--navy); }
  .brand-name { font-family: "Jost", sans-serif; font-weight: 500; font-size: 42px; color: var(--navy); letter-spacing: 1px; }

  /* Hero */
  .hero { position: absolute; top: 145px; left: 0; width: 927px; height: 387px; background: var(--hero); }
  .hero-photo { position: absolute; top: 0; right: 0; width: 540px; height: 387px; background: linear-gradient(100deg, var(--hero) 0%, #2a3f6b 45%, #233559 75%, #1a2a4d 100%); }
  .notch { position: absolute; left: 50%; width: 0; height: 0; transform: translateX(-50%); border-left: 12px solid transparent; border-right: 12px solid transparent; }
  .notch-down-white { top: 145px; border-top: 13px solid var(--white); }
  .notch-down-hero { top: 532px; border-top: 13px solid var(--hero); }
  .notch-down-band { top: 876px; border-top: 13px solid var(--white); }
  .headline { position: absolute; left: 31px; top: 255px; color: var(--white); font-family: "Jost", sans-serif; }
  .headline-line1 { font-size: 37px; font-weight: 400; letter-spacing: 1px; line-height: 42px; }
  .headline-line2 { font-size: 39px; font-weight: 700; letter-spacing: 1px; line-height: 42px; }
  .fee-box { position: absolute; left: 31px; top: 344px; width: 347px; height: 29px; background: var(--white); color: var(--navy); font-family: "Jost", sans-serif; font-weight: 500; font-size: 21px; letter-spacing: 2.5px; display: flex; align-items: center; justify-content: center; }

  /* Offer list */
  .offer-title { position: absolute; left: 346px; top: 582px; width: 225px; height: 43px; background: var(--navy); color: var(--white); font-family: "Jost", sans-serif; font-size: 24px; display: flex; align-items: center; justify-content: center; box-shadow: 0 4px 0 var(--grey-line); }
  .offer-list { position: absolute; list-style: none; }
  .offer-list.left { left: 27px; top: 652px; }
  .offer-list.right { left: 524px; top: 652px; }
  .offer-list li { display: flex; align-items: flex-start; font-size: 18.5px; line-height: 33.3px; }
  .offer-list .tick { width: 16px; height: 16px; margin-top: 8px; margin-right: 16px; flex: none; }

  /* Feature band */
  .feature-band { position: absolute; top: 876px; left: 0; width: 927px; height: 229px; background: linear-gradient(180deg, #253d6f, #213764); }
  .feature { position: absolute; top: 35px; text-align: center; color: var(--white); font-family: "Jost", sans-serif; font-size: 18.5px; line-height: 24px; }
  .feature svg { display: block; margin: 0 auto 20px; width: 74px; height: 74px; }
  .divider { position: absolute; top: 45px; height: 70px; border-left: 1px dashed rgba(255,255,255,0.5); }

  /* Footer */
  .address-tab { position: absolute; left: 356px; top: 1085px; width: 213px; height: 44px; }
  .address-tab span { position: absolute; inset: 0; display: flex; align-items: center; justify-content: center; font-family: "Jost", sans-serif; font-weight: 500; font-size: 25px; color: var(--navy); }
  .contact { position: absolute; top: 1105px; left: 0; width: 927px; height: 95px; background: var(--grey); z-index: -0; }
  .contact-row { position: absolute; top: 47px; left: 30px; right: 30px; display: flex; align-items: center; justify-content: space-between; color: var(--navy); font-weight: 700; font-size: 17px; }
  .contact-item { display: flex; align-items: center; gap: 8px; }
  .contact-item.phone { font-size: 23px; }
  .sep { color: var(--navy); font-weight: 400; }
</style>
</head>
<body>
<div class="flyer">
  <header class="brand">
    <span class="brand-mark"></span>
    <span class="brand-name">Marlow Realty</span>
  </header>

  <section class="hero">
    <div class="hero-photo" role="img" aria-label="Agent in a navy suit holding a small model house on his open hand"></div>
  </section>
  <div class="notch notch-down-white"></div>
  <div class="notch notch-down-hero"></div>
  <div class="headline">
    <div class="headline-line1">100% COMMISSION</div>
    <div class="headline-line2">NO MONTHLY FEE</div>
  </div>
  <div class="fee-box">$450 Flat Transaction Fee</div>

  <h2 class="offer-title">What We Offer</h2>
  <svg width="0" height="0" style="position:absolute">
    <symbol id="tick" viewBox="0 0 16 16"><path d="M13 8.5V14H2V3h8" fill="none" stroke="#1f3a6e" stroke-width="1.8"/><path d="M5 7l3 3 7-7" fill="none" stroke="#1f3a6e" stroke-width="1.8"/></symbol>
  </svg>
  <ul class="offer-list left">
    <li><svg class="tick"><use href="#tick"/></svg>24/7 Office Access</li>
    <li><svg class="tick"><use href="#tick"/></svg>Free E &amp; O Insurance for 1st Year</li>
    <li><svg class="tick"><use href="#tick"/></svg>Free Online CE and PLE</li>
    <li><svg class="tick"><use href="#tick"/></svg>Free 1,000 Business Cards</li>
    <li><svg class="tick"><use href="#tick"/></svg>Free Professional Social Media Marketing</li>
    <li><svg class="tick"><use href="#tick"/></svg>Free Printing, Scanning, and Copies</li>
  </ul>
  <ul class="offer-list right">
    <li><svg class="tick"><use href="#tick"/></svg>Free Buyer and Seller Presentation Packages</li>
    <li><svg class="tick"><use href="#tick"/></svg><span>Free Filquay Cloud Based Document<br>Management Access</span></li>
    <li><svg class="tick"><use href="#tick"/></svg>Access to our Internal Brokerage Forum</li>
    <li><svg class="tick"><use href="#tick"/></svg>Company Profit Sharing!</li>
    <li><svg class="tick"><use href="#tick"/></svg>Private Offices Available to Rent</li>
  </ul>

  <section class="feature-band">
    <div class="feature" style="left:10px;width:210px">
      <svg viewBox="0 0 74 74" fill="none" stroke="#fff" stroke-width="2.5"><path d="M14 28l10-12h26l10 12-23 28z"/><path d="M14 28h46M30 16l-6 12 13 28M44 16l6 12"/><circle cx="43" cy="44" r="10" fill="#243b6c"/><path d="M50 51l9 9"/></svg>
      Lead Generation<br>Sofvtware with over<br>3,000 Leads
    </div>
    <div class="divider" style="left:248px"></div>
    <div class="feature" style="left:268px;width:170px">
      <svg viewBox="0 0 74 74" fill="none" stroke="#fff" stroke-width="2.5"><path d="M37 6c10 10 12 24 8 40H29C25 30 27 16 37 6z"/><path d="M29 36l-8 12h10M45 36l8 12H43"/><path d="M33 54v8M37 54v12M41 54v8"/></svg>
      10 Leads to<br>Start
    </div>
    <div class="divider" style="left:458px"></div>
    <div class="feature" style="left:472px;width:220px">
      <svg viewBox="0 0 74 74" fill="none" stroke="#fff" stroke-width="2.5"><rect x="10" y="10" width="54" height="54"/><path d="M10 20h54"/><path d="M20 48a17 17 0 0 1 34 0"/><circle cx="37" cy="42" r="6"/></svg>
      Free Personal CRM<br>and Website
    </div>
    <div class="divider" style="left:706px"></div>
    <div class="feature" style="left:730px;width:190px">
      <svg viewBox="0 0 74 74" fill="none" stroke="#fff" stroke-width="2.5"><circle cx="37" cy="30" r="16"/><circle cx="14" cy="14" r="6"/><circle cx="60" cy="44" r="6"/><path d="M31 24v12M37 22v16M43 26v10"/><rect x="27" y="52" width="20" height="14"/><path d="M37 52v14"/></svg>
      Restrictions and<br>Rules apply
    </div>
  </section>
  <div class="notch notch-down-band"></div>

  <footer class="contact">
    <div class="contact-row">
      <span class="contact-item">
        <svg width="16" height="20" viewBox="0 0 16 20"><path d="M8 0a7 7 0 0 0-7 7c0 5 7 13 7 13s7-8 7-13a7 7 0 0 0-7-7z" fill="#1f3a6e"/><circle cx="8" cy="7" r="2.5" fill="#d9dadd"/></svg>
        4817 Amberfield Road, Suite 512, Fairfax, VA 22194
      </span>
      <span class="sep">|</span>
      <span class="contact-item phone">
        <svg width="20" height="20" viewBox="0 0 20 20"><path d="M4 1l4 4-2 3c1 3 3 5 6 6l3-2 4 4-3 3C9 19 1 11 1 4z" fill="none" stroke="#1f3a6e" stroke-width="2"/></svg>
        703-555-0147
      </span>
      <span class="sep">|</span>
      <span class="contact-item">
        <svg width="22" height="15" viewBox="0 0 22 15"><rect width="22" height="15" rx="1" fill="#1f3a6e"/><path d="M1 1l10 8 10-8" fill="none" stroke="#d9dadd" stroke-width="1.6"/></svg>
        info@marlowrealty.example
      </span>
    </div>
  </footer>
  <div class="address-tab">
    <svg width="213" height="44" viewBox="0 0 213 44"><polygon points="14,0 199,0 213,22 199,44 14,44 0,22" fill="#fff"/></svg>
    <span>Address</span>
  </div>
</div>
</body>
</html>
```